Car dent,ding,crease removal. This will be for the Automotive industry, bodywork repair.

I need a double sided business card designing.

Company name is Panel Mender and we remove small car park dents creases and dings.

The card should have sleek car design/outline on it.

The wording Paintless Dent Removal to be on the card.

The background colours used should include Royal blue, black, and a hint of red.

Need a sleek modern look, clean lines.

I really don't want designers going to my website and just copying the car design, I want something new!

Reason: I've put a guaranteed payment on the design now.

Industry/Entity Type

Automotive

Requirements
Must have
• Paintless Dent Removal
Panel Mender
Gareth Holloway
enquiries@panelmender.example.co.uk
07700954316
Covering, Chester, North Wales and the Wirral
Free quotes available
www.panelmender.example.co.uk

```html
<!DOCTYPE html>
<html lang="en">
<head>
<meta charset="utf-8">
<title>Panel Mender – Business Card</title>
<link rel="stylesheet" href="https://fonts.googleapis.com/css2?family=Roboto+Slab:wght@700&family=Open+Sans:wght@400;600&display=swap">
<style>
  :root {
    --backdrop: #cde8df;
    --card-blue: #0a50dc;
    --card-blue-deep: #0043cf;
    --white: #ffffff;
    --accent-red: #e0212b;
    --sketch-tone: #4f80ea;
  }
  * { box-sizing: border-box; margin: 0; padding: 0; }
  html, body {
    width: 1200px; height: 856px; overflow: hidden;
    background: var(--backdrop);
  }
  .sheet {
    width: 1200px; height: 856px;
    display: flex; align-items: center; justify-content: center; gap: 60px;
  }
  .card {
    position: relative;
    width: 510px; height: 292px;
    border-radius: 38px;
    background: linear-gradient(180deg, var(--card-blue) 0%, var(--card-blue-deep) 100%);
    color: var(--white);
    overflow: hidden;
    box-shadow: 0 14px 30px rgba(20, 60, 60, 0.18);
  }

  /* Front */
  .card-front .car-sketch {
    position: absolute; left: 120px; top: 74px;
    width: 290px; height: 100px;
    border-radius: 50px 50px 8px 8px;
    background: linear-gradient(180deg, var(--sketch-tone), var(--card-blue));
  }
  .card-front .accent-rule {
    position: absolute; left: 128px; top: 176px;
    width: 286px; height: 4px;
    background: var(--accent-red);
    transform: rotate(-5deg);
    transform-origin: left center;
  }
  .card-front .brand-name {
    position: absolute; left: 0; right: 0; top: 190px;
    text-align: center;
    font: 700 24px/1 "Roboto Slab", serif;
    letter-spacing: 0.22em;
  }

  /* Back */
  .card-back { text-align: center; padding-top: 44px; }
  .card-back .person-name {
    font: 700 22px/1 "Roboto Slab", serif;
    letter-spacing: 0.04em;
  }
  .card-back .person-role {
    margin-top: 6px;
    font: 600 9px/1 "Open Sans", sans-serif;
    letter-spacing: 0.1em;
  }
  .contact-list {
    list-style: none;
    margin: 30px auto 0;
    display: inline-flex; flex-direction: column; gap: 5px;
    font: 400 12px/1.3 "Open Sans", sans-serif;
  }
  .contact-list .contact-line {
    display: flex; align-items: center; justify-content: center; gap: 8px;
  }
  .contact-icon { width: 13px; height: 13px; flex: none; }
  .service-notes {
    margin-top: 8px;
    font: 400 12px/1.35 "Open Sans", sans-serif;
  }
</style>
</head>
<body>
<main class="sheet">
  <section class="card card-front" aria-label="Business card front">
    <div class="car-sketch" role="img" aria-label="Sleek white line drawing of a sports car in side profile"></div>
    <div class="accent-rule"></div>
    <p class="brand-name">PANEL MENDER</p>
  </section>

  <section class="card card-back" aria-label="Business card back">
    <h1 class="person-name">GARETH HOLLOWAY</h1>
    <p class="person-role">PAINTLESS DENT REMOVAL / PANEL MENDER</p>
    <ul class="contact-list">
      <li class="contact-line">
        <svg class="contact-icon" viewBox="0 0 16 16" aria-hidden="true">
          <path fill="var(--accent-red)" d="M3.6 1.5l2.3 2.6-1.3 1.8c.9 2 2.5 3.6 4.5 4.5l1.8-1.3 2.6 2.3-1.2 2.2c-5.6-.3-10.4-5.1-10.7-10.7z"/>
        </svg>
        <span>077-009-543-16</span>
      </li>
      <li class="contact-line">
        <svg class="contact-icon" viewBox="0 0 16 16" aria-hidden="true">
          <rect x="1" y="3" width="14" height="10" rx="1" fill="var(--accent-red)"/>
          <path d="M1.5 3.8L8 9l6.5-5.2" stroke="var(--white)" stroke-width="1.2" fill="none"/>
        </svg>
        <span>enquiries@panelmender.example.co.uk</span>
      </li>
    </ul>
    <p class="service-notes">
      Covering, Chester, North Wales<br>
      and the Wirral<br>
      Free quotes available<br>
      www.panelmender.example.co.uk
    </p>
  </section>
</main>
</body>
</html>
```